Family Ranch with a hobby vineyard needs 2 wine labels for our first harvest

Design 2 wine labels (front and back) with the Brindor Ranch logo.
Label 1:
Sauvignon Blanc
Alc. 12.5% by Vol.
Palos Verdes Peninsula - add as the region
Year 2022
Label 2:
Cabernet Sauvignon
Alc. 13.5% by Vol.
Year 2022
For the back label design:
GOVERNMENT WARNING: (1) According to the Surgeon General, women
should not drink alcoholic beverages during pregnancy because of the risk of
birth defects. (2) Consumption of alcoholic beverages impairs your ability to
drive a car or operate machinery, and may cause health problems.
Contains Sulfates.
750ML
I just received the bottles and have attached a picture.
Look and feel
Each slider illustrates characteristics of the customer's brand and the style your logo design should communicate.

```html
<!DOCTYPE html>
<html lang="en">
<head>
<meta charset="utf-8">
<title>Brindor Ranch – Wine Labels</title>
<link href="https://fonts.googleapis.com/css2?family=Playfair+Display:wght@400&family=Cormorant+SC:wght@500&display=swap" rel="stylesheet">
<style>
  :root {
    --page: #ffffff;
    --paper: #f1f0ee;
    --paper-shade: #e6e5e2;
    --night: #2a2a2b;
    --gold: #b8862f;
    --gold-light: #e2b552;
    --gold-deep: #7d4f17;
    --ink: #4a4a4a;
    --sketch: #9a9a98;
  }
  html, body {
    margin: 0;
    width: 1200px;
    height: 1200px;
    overflow: hidden;
    background: var(--page);
  }
  .canvas {
    position: relative;
    width: 1200px;
    height: 1200px;
  }
  .label {
    position: absolute;
    top: 170px;
    width: 400px;
    height: 860px;
    background: linear-gradient(90deg, var(--paper-shade), var(--paper) 12%, var(--paper) 88%, var(--paper-shade));
    box-shadow: 0 10px 30px rgba(0,0,0,0.12);
    overflow: hidden;
    text-align: center;
  }
  .label--blanc { left: 150px; }
  .label--cabernet { left: 650px; }

  .label__dark {
    position: absolute;
    left: 0; top: 0;
    width: 100%;
    height: 500px;
    background: var(--night);
  }

  .brand {
    position: absolute;
    left: 0; width: 100%;
    font-family: "Playfair Display", serif;
    font-weight: 400;
    color: var(--gold);
  }
  .brand__dot {
    display: block;
    width: 70px; height: 70px;
    margin: 0 auto 18px;
    border-radius: 50%;
    background: var(--gold);
  }
  .brand__name {
    display: block;
    font-size: 40px;
    line-height: 1.05;
    letter-spacing: 2px;
  }
  .label--blanc .brand { top: 60px; }
  .label--cabernet .brand { top: 90px; }

  .varietal {
    position: absolute;
    left: 0; width: 100%;
    margin: 0;
    font-family: "Playfair Display", serif;
    font-weight: 400;
    font-size: 52px;
    line-height: 1.05;
    color: var(--gold);
    transform: scaleX(0.82);
  }
  .label--blanc .varietal { top: 340px; }
  .label--cabernet .varietal { top: 340px; }

  .origin {
    position: absolute;
    left: 0; width: 100%;
    font-family: "Cormorant SC", serif;
    font-weight: 500;
    font-size: 22px;
    line-height: 1.4;
    color: var(--ink);
    letter-spacing: 0.5px;
  }
  .label--blanc .origin { top: 508px; }
  .label--cabernet .origin { top: 518px; }

  .landscape {
    position: absolute;
    left: 0; width: 100%;
    bottom: 44px;
    background: linear-gradient(180deg, rgba(241,240,238,0) 0%, #d9d9d6 35%, var(--sketch) 70%, #bdbdba 100%);
  }
  .label--blanc .landscape { height: 230px; }
  .label--cabernet .landscape { height: 220px; }

  .abv {
    position: absolute;
    right: 12px;
    bottom: 50px;
    font-family: "Cormorant SC", serif;
    font-weight: 500;
    font-size: 11px;
    color: #555;
  }

  .gold-band {
    position: absolute;
    left: 0; bottom: 14px;
    width: 100%;
    height: 18px;
    background: linear-gradient(90deg, var(--gold-deep), var(--gold-light) 30%, var(--gold) 60%, var(--gold-deep));
  }
</style>
</head>
<body>
<main class="canvas">

  <section class="label label--blanc">
    <div class="brand">
      <span class="brand__dot"></span>
      <span class="brand__name">BRINDOR<br>RANCH</span>
    </div>
    <h1 class="varietal">SAUVIGNON<br>BLANC</h1>
    <p class="origin">Palos Verdes Peninsula<br>Year 2022</p>
    <div class="landscape" role="img" aria-label="Pencil sketch of a coastal ranch with palm trees overlooking the ocean"></div>
    <span class="abv">Alc. 12.5% by Vol.</span>
    <div class="gold-band"></div>
  </section>

  <section class="label label--cabernet">
    <div class="label__dark"></div>
    <div class="brand">
      <span class="brand__dot"></span>
      <span class="brand__name">BRINDOR<br>RANCH</span>
    </div>
    <h1 class="varietal">CABERNET<br>SAUVIGNON</h1>
    <p class="origin">Palos Verdes Peninsula<br>Year 2022</p>
    <div class="landscape" role="img" aria-label="Pencil sketch of a coastal ranch with palm trees overlooking the ocean"></div>
    <span class="abv">Alc. 13.5% by Vol.</span>
    <div class="gold-band"></div>
  </section>

</main>
</body>
</html>
```